KELU Nature Soap

We need to design new product Nature and medicative Soap.Made in Malaysia
* 100% natural.
* made from nature Tropic oil.
* Very effective for Acne & Skin irritation
* size 100 Gm.
* Use for all skin types including sensitive skin
* Name of the product " KELU Soap"

Reason: please I need to extended since I haven't receive any suitable design for my project

Target Market(s)

International

Industry/Entity Type

Hair And Beauty

Font styles to use
Serif

Colors
33a6d7
abd037
fbed22

Requirements
Must have
• * must have English- Arabic ingredient
• * Very effective for Acne & Skin irritation
Nice to have
• * some things related to natural (water,tree,face..)
• * Show faces picture (after - before)

```html
<!DOCTYPE html>
<html lang="en">
<head>
<meta charset="utf-8">
<title>KELU Soap – pack front</title>
<link href="https://fonts.googleapis.com/css2?family=Roboto+Condensed:ital,wght@0,300;0,700;1,700&display=swap" rel="stylesheet">
<style>
  :root {
    --stage: #e8e8e8;
    --cream: #fdf3e2;
    --cream-light: #fffaf2;
    --navy: #1f4f9c;
    --brown: #7a2a10;
    --leaf-green: #6db33f;
    --white: #ffffff;
    --water-light: #c9d9f0;
    --water: #7f9fd6;
    --skin-light: #f3dccb;
    --skin: #e2b49b;
    --hair: #a68470;
    --peach: #f6b9a3;
    --ingredient-warm: #ead8c4;
    --ingredient-cool: #cfe3d0;
  }
  * { margin: 0; padding: 0; box-sizing: border-box; }
  html, body { width: 1200px; height: 1164px; overflow: hidden; }
  body {
    background: var(--stage);
    font-family: "Roboto Condensed", Arial, sans-serif;
    position: relative;
  }
  .pack-front {
    position: absolute;
    left: 150px;
    width: 900px;
    height: 547px;
    overflow: hidden;
    background: linear-gradient(90deg, var(--cream) 0%, var(--cream-light) 70%, var(--cream) 100%);
  }
  .pack-front--classic { top: 25px; }
  .pack-front--before-after { top: 592px; }

  .model-photo {
    position: absolute;
    left: 530px; top: 0;
    width: 370px; height: 547px;
    background: linear-gradient(180deg, var(--hair) 0%, var(--skin-light) 30%, var(--skin-light) 60%, var(--skin) 100%);
    opacity: 0.75;
  }
  .after-panel {
    position: absolute;
    right: 0; top: 0;
    width: 150px; height: 547px;
    background: linear-gradient(90deg, rgba(246,185,163,0.35), var(--peach));
  }

  .water-wave {
    position: absolute; left: 0; bottom: 0;
    width: 900px; height: 200px;
  }

  .ingredients-art {
    position: absolute;
    left: 40px; top: 320px;
    width: 330px; height: 200px;
    border-radius: 12px;
    background: linear-gradient(135deg, var(--ingredient-cool) 0%, var(--ingredient-warm) 100%);
  }

  .brand {
    position: absolute;
    left: 32px; top: 60px;
    display: flex; align-items: center; gap: 16px;
  }
  .brand-dot {
    width: 58px; height: 58px; border-radius: 50%;
    background: var(--navy);
  }
  .brand-name {
    font-size: 60px; font-weight: 700; color: var(--navy);
    line-height: 1;
  }

  .claim {
    position: absolute;
    left: 48px; top: 182px;
    color: var(--brown);
    font-size: 35px; line-height: 43px;
    text-transform: uppercase;
  }
  .claim-lead { font-weight: 300; display: block; }
  .claim-focus { font-weight: 700; display: block; }

  .oil-badge {
    position: absolute;
    left: 275px; top: 297px;
    width: 140px; height: 140px; border-radius: 50%;
    background: var(--leaf-green);
    color: var(--white);
    display: flex; flex-direction: column; align-items: center; justify-content: center;
    font-style: italic; font-weight: 700;
    font-size: 29px; line-height: 30px;
    text-align: center;
  }
  .pack-front--before-after .claim { top: 176px; }
  .pack-front--before-after .oil-badge { left: 262px; top: 312px; width: 136px; height: 136px; }
</style>
</head>
<body>

  <section class="pack-front pack-front--classic">
    <div class="model-photo" role="img" aria-label="Photo of a woman with clear skin resting her chin on her hand"></div>
    <svg class="water-wave" role="img" aria-label="Flowing blue water wave" viewBox="0 0 900 200" preserveAspectRatio="none">
      <defs>
        <linearGradient id="waveA" x1="0" y1="0" x2="1" y2="0">
          <stop offset="0" stop-color="#7f9fd6" stop-opacity="0.8"/>
          <stop offset="1" stop-color="#c9d9f0" stop-opacity="0.8"/>
        </linearGradient>
      </defs>
      <path d="M0 40 C200 60 400 90 600 120 C720 138 820 150 900 150 L900 200 L0 200 Z" fill="url(#waveA)"/>
    </svg>
    <div class="ingredients-art" role="img" aria-label="Illustration of split coconut with white tropical flowers and leaves"></div>

    <div class="brand">
      <span class="brand-dot"></span>
      <span class="brand-name">KELU Soap</span>
    </div>
    <p class="claim">
      <span class="claim-lead">Very effective for</span>
      <span class="claim-focus">Acne &amp; Skin Irritation</span>
    </p>
    <div class="oil-badge"><span>Natural</span><span>Tropic</span><span>Oil</span></div>
  </section>

  <section class="pack-front pack-front--before-after">
    <div class="model-photo" role="img" aria-label="Before and after photo of a woman's face, one half clear, one half with acne spots"></div>
    <div class="after-panel"></div>
    <svg class="water-wave" role="img" aria-label="Flowing blue water wave" viewBox="0 0 900 200" preserveAspectRatio="none">
      <defs>
        <linearGradient id="waveB" x1="0" y1="0" x2="1" y2="0">
          <stop offset="0" stop-color="#7f9fd6" stop-opacity="0.8"/>
          <stop offset="1" stop-color="#c9d9f0" stop-opacity="0.8"/>
        </linearGradient>
      </defs>
      <path d="M0 40 C200 60 400 90 600 120 C720 138 820 150 900 150 L900 200 L0 200 Z" fill="url(#waveB)"/>
    </svg>
    <div class="ingredients-art" role="img" aria-label="Illustration of split coconut with white tropical flowers, leaves and a water splash"></div>

    <div class="brand">
      <span class="brand-dot"></span>
      <span class="brand-name">KELU Soap</span>
    </div>
    <p class="claim">
      <span class="claim-lead">Very effective for</span>
      <span class="claim-focus">Acne &amp; Skin Irritation</span>
    </p>
    <div class="oil-badge"><span>Natural</span><span>Tropic</span><span>Oil</span></div>
  </section>

</body>
</html>
```